New Business Cards for NYC Salon

We are updating all of our cards. 7142-2869-4057 is my account number. We put names of our stylists on their cards. The back should include appointment space. Were looking for something more sleek and modern. Black/White Silver... or even touches of the orange color on our website which has been our thing for years. The design should communicate professional upscale boutique salon for men and women. Should be able to incorporate design into thank you cards, referral cards, brochure and postcards. The file is a zip file...we like the stacked ones black or white or the side versions.

Industry/Entity Type

Beauty Salon

Contact Information for Business Card

Marcus John's Salon313 W. 53rd Street, New York NY 10019 212-386-7714 info@marcusdellsalon.example www.marcusdellsalon.example

Font styles to use
Other font styles liked:
• trajan

Requirements
Must have
• we print a different card for every person in the salon. Begin by designing with the name Marcus. We will change it with every employee when printing. Must have a space for appointment date and time.
Nice to have
• Were looking to move towards the stacked or side placed logo but not opposed to utilizing the circular.
Should not have
• Photos

```html
<!DOCTYPE html>
<html lang="en">
<head>
<meta charset="utf-8">
<title>Marcus Dell's Salon — Business Card</title>
<link rel="stylesheet" href="https://fonts.googleapis.com/css2?family=Cinzel:wght@400;600&family=Open+Sans:wght@400;600&display=swap">
<style>
  :root {
    --orange: #f47f1c;
    --orange-deep: #ec7410;
    --white: #ffffff;
    --ink: #1d1d1d;
    --rule: #d9d9d9;
    --backdrop: #e4e4e6;
    --muted: #555555;
  }
  * { box-sizing: border-box; margin: 0; padding: 0; }
  html, body { width: 1200px; height: 800px; overflow: hidden; }
  body {
    background: var(--backdrop);
    font-family: "Cinzel", serif;
    position: relative;
  }
  .card {
    position: absolute;
    width: 560px;
    height: 320px;
    top: 240px;
    border-radius: 4px;
    overflow: hidden;
  }

  /* ---------- Back: appointment card ---------- */
  .card-back { left: 30px; background: var(--white); }
  .back-mark {
    position: absolute; left: 28px; top: 24px;
    width: 84px; height: 84px; border-radius: 50%;
    background: var(--orange);
    display: flex; align-items: center; justify-content: center;
    text-align: center;
    font-size: 10px; line-height: 1.25; letter-spacing: 1px;
    color: var(--ink);
  }
  .appt-form { position: absolute; left: 140px; right: 30px; top: 40px; }
  .field {
    display: flex; align-items: flex-end; gap: 10px;
    font-size: 13px; letter-spacing: 0.5px; color: var(--ink);
    height: 40px;
  }
  .field .line { flex: 1; border-bottom: 1px solid var(--rule); height: 1px; margin-bottom: 4px; }
  .field .short { flex: 0 0 150px; }
  .field-note { height: 34px; }
  .back-band {
    position: absolute; left: 0; right: 0; bottom: 0; height: 62px;
    background: var(--orange);
    display: flex; align-items: center; justify-content: flex-end; gap: 12px;
    padding-right: 32px;
    font-family: "Open Sans", sans-serif; font-size: 30px; color: var(--ink);
  }

  /* ---------- Front: stylist card ---------- */
  .card-front { left: 610px; background: linear-gradient(135deg, var(--orange), var(--orange-deep)); color: var(--white); }
  .front-mark {
    position: absolute; left: 40px; top: 22px;
    width: 160px; height: 160px; border-radius: 50%;
    background: var(--white);
    display: flex; align-items: center; justify-content: center; text-align: center;
    font-size: 16px; line-height: 1.3; letter-spacing: 2px; color: var(--ink);
  }
  .tagline {
    position: absolute; left: 240px; top: 26px; width: 240px;
    font-size: 11.5px; font-weight: 600; letter-spacing: 0.5px; color: var(--ink);
    text-align: right;
  }
  .stylists { position: absolute; left: 250px; top: 52px; width: 230px; list-style: none; }
  .stylists li {
    display: flex; justify-content: space-between; align-items: center;
    height: 25px; font-size: 14px; color: var(--ink); letter-spacing: 0.5px;
  }
  .stylists .tick { width: 8px; height: 2px; background: var(--white); }
  .rule-h { position: absolute; left: 18px; top: 212px; width: 474px; height: 1px; background: var(--white); }
  .rule-v { position: absolute; left: 492px; top: 60px; width: 1px; height: 240px; background: var(--white); }
  .contact {
    position: absolute; left: 26px; top: 224px; list-style: none;
    font-family: "Open Sans", sans-serif; font-size: 13px; color: var(--white);
  }
  .contact li { display: flex; align-items: center; gap: 8px; height: 26px; }
  .contact .dot { width: 10px; height: 10px; border: 1.5px solid var(--ink); border-radius: 50%; }
  .front-phone {
    position: absolute; left: 526px; top: 160px;
    transform: translate(-50%, -50%) rotate(90deg);
    display: flex; align-items: center; gap: 10px; white-space: nowrap;
    font-family: "Open Sans", sans-serif; font-size: 26px; color: var(--white);
  }
  .icon-phone { width: 26px; height: 26px; }
</style>
</head>
<body>

  <section class="card card-back" aria-label="Appointment card, back">
    <div class="back-mark">Marcus Dell's<br>Salon</div>
    <div class="appt-form">
      <div class="field">Name <span class="line"></span></div>
      <div class="field field-note">has an appointment on</div>
      <div class="field">Date <span class="line"></span> Time <span class="line short"></span></div>
      <div class="field"><span class="line"></span></div>
    </div>
    <div class="back-band">
      <svg class="icon-phone" viewBox="0 0 24 24" aria-hidden="true">
        <circle cx="12" cy="12" r="11" fill="none" stroke="#1d1d1d" stroke-width="1.6"/>
        <path d="M8.5 6.5c.6-.4 1.2-.2 1.5.3l1 1.8c.3.5.1 1-.3 1.3l-.7.5c.6 1.3 1.6 2.4 2.9 3l.5-.7c.3-.4.9-.6 1.3-.3l1.8 1c.5.3.7.9.3 1.5-.7 1-1.8 1.4-3 .9-2.7-1.1-4.8-3.2-5.9-5.9-.4-1.2 0-2.3.6-3.4z" fill="#1d1d1d"/>
      </svg>
      <span>212-386-7714</span>
    </div>
  </section>

  <section class="card card-front" aria-label="Stylist card, front">
    <div class="front-mark">Marcus Dell's<br>Salon</div>
    <p class="tagline">INDIVIDUALIZED FOR EACH STYLIST</p>
    <ul class="stylists">
      <li><span class="tick"></span>MARCUS</li>
      <li><span class="tick"></span>LENA</li>
      <li><span class="tick"></span>IRIS</li>
      <li><span class="tick"></span>JOSEPHINE</li>
      <li><span class="tick"></span>VALENTINO</li>
      <li><span class="tick"></span>NADIA</li>
    </ul>
    <div class="rule-h"></div>
    <div class="rule-v"></div>
    <ul class="contact">
      <li><span class="dot"></span>748 E. 29th Street, New York NY 10016</li>
      <li><span class="dot"></span>www.marcusdellsalon.example</li>
      <li><span class="dot"></span>info@marcusdellsalon.example</li>
    </ul>
    <div class="front-phone">
      <svg class="icon-phone" viewBox="0 0 24 24" aria-hidden="true">
        <circle cx="12" cy="12" r="11" fill="none" stroke="#1d1d1d" stroke-width="1.6"/>
        <path d="M8.5 6.5c.6-.4 1.2-.2 1.5.3l1 1.8c.3.5.1 1-.3 1.3l-.7.5c.6 1.3 1.6 2.4 2.9 3l.5-.7c.3-.4.9-.6 1.3-.3l1.8 1c.5.3.7.9.3 1.5-.7 1-1.8 1.4-3 .9-2.7-1.1-4.8-3.2-5.9-5.9-.4-1.2 0-2.3.6-3.4z" fill="#1d1d1d"/>
      </svg>
      <span>212-386-7714</span>
    </div>
  </section>

</body>
</html>
```